Business Card Design

Buy and sell properties
Buy and rehab properties
Buy properties for cash
That is what I do but do need a logo
looking for some type of logo or design on it
Just started business
Back of card should say something like BUY HOUSES CASH
Overview: it is a new company. Basically I buy properties wholesale and fix them up and sell them or sell them to other fix and flippers
Background: company is new so not any background
Market: is basically anyone selling a house or buying a house. Someone that needs to sell house fast. Basically I am a cash home buyer!!!

Updates
Email on card should be:   harborlanerealtyinc@mailbox.test

Industry/Entity Type
House
Contact Information for Business Card
Harbor Lane Realty Inc
PO Box 718269
Cedar Marsh FL 32987

Dale Morrick
harborlanerealtyinc@mailbox.test
555-271-6094

```html
<!DOCTYPE html>
<html lang="en">
<head>
<meta charset="utf-8">
<title>Harbor Lane Realty Inc – Business Card</title>
<link rel="stylesheet" href="https://fonts.googleapis.com/css2?family=Cinzel:wght@600;800&family=Arimo:wght@400;700&display=swap">
<style>
  :root {
    --ink: #0d0d0d;
    --paper: #ffffff;
    --navy: #2e3192;
    --orange: #f7941d;
    --stage: #e6e4e1;
    --skyline-top: #3a3a3a;
    --display: "Cinzel", serif;
    --body: "Arimo", Arial, sans-serif;
  }
  * { box-sizing: border-box; margin: 0; padding: 0; }
  html, body { width: 1200px; height: 1200px; overflow: hidden; }
  body { background: var(--stage); position: relative; font-family: var(--body); }

  .card {
    position: absolute;
    top: 124px;
    width: 571px;
    height: 976px;
    background: var(--paper);
    overflow: hidden;
    box-shadow: 0 6px 18px rgba(0,0,0,.18);
  }
  .card--front { left: 19px; }
  .card--back { left: 610px; }

  .top-stripe { position: absolute; top: 0; left: 0; width: 100%; height: 22px; display: flex; }
  .top-stripe span { height: 100%; }
  .stripe-black { background: var(--ink); }
  .stripe-orange { background: var(--orange); }
  .stripe-navy { background: var(--navy); }

  .brand-mark {
    position: absolute; left: 50%; top: 84px;
    width: 150px; height: 150px; margin-left: -75px;
    border-radius: 50%; background: var(--navy);
  }
  .brand-name {
    position: absolute; left: 0; width: 100%; top: 298px;
    text-align: center; font-family: var(--display); font-weight: 600;
    color: var(--ink); line-height: 1;
  }
  .brand-name .line-main { display: block; font-size: 60px; letter-spacing: 1px; }
  .brand-name .line-sub { display: block; font-size: 36px; margin-top: 12px; letter-spacing: 1px; }

  .slogan {
    position: absolute; left: 0; width: 100%; top: 560px;
    text-align: center; font-family: var(--display); font-weight: 800;
    font-size: 34px; color: var(--ink); letter-spacing: 0.5px;
  }

  .skyline-art {
    position: absolute; left: 0; top: 662px; width: 100%; height: 188px;
    background: linear-gradient(to bottom, var(--skyline-top), var(--ink));
  }
  .services {
    position: absolute; left: 0; top: 848px; width: 100%; height: 128px;
    background: var(--ink); list-style: none; padding-top: 14px;
  }
  .services li {
    display: flex; align-items: center; height: 33px;
    color: var(--paper); font-size: 23px; letter-spacing: 0.3px;
  }
  .services li::before {
    content: ""; width: 134px; height: 18px; background: var(--orange);
    margin-right: 27px; flex: none;
  }

  .back-panel { position: absolute; left: 0; top: 0; width: 100%; height: 100%; }
  .contact {
    position: absolute; left: 0; top: 600px; width: 100%;
    text-align: center; color: var(--paper);
  }
  .contact .person { font-size: 44px; line-height: 1; }
  .contact .title { font-size: 32px; font-weight: 700; color: var(--orange); margin-top: 22px; line-height: 1; }
  .contact .address { font-size: 32px; line-height: 44px; margin-top: 40px; }
  .contact .reach { font-size: 31px; line-height: 50px; margin-top: 22px; white-space: nowrap; }
  .contact .reach .email { font-size: 26px; }
</style>
</head>
<body>

<section class="card card--front">
  <div class="top-stripe">
    <span class="stripe-black" style="width:139px"></span>
    <span class="stripe-orange" style="width:67px"></span>
    <span class="stripe-navy" style="width:156px"></span>
    <span class="stripe-orange" style="width:68px"></span>
    <span class="stripe-black" style="width:141px"></span>
  </div>
  <div class="brand-mark"></div>
  <h1 class="brand-name"><span class="line-main">HARBOR LANE</span><span class="line-sub">REALTY INC</span></h1>
  <p class="slogan">BUY HOUSES CA$H</p>
  <div class="skyline-art" role="img" aria-label="City skyline silhouette of black high-rise buildings"></div>
  <ul class="services">
    <li>BUY AND SELL PROPERTIES</li>
    <li>BUY AND REHAB PROPERTIES</li>
    <li>BUY PROPERTIES FOR CASH</li>
  </ul>
</section>

<section class="card card--back">
  <svg class="back-panel" viewBox="0 0 571 976" width="571" height="976" aria-hidden="true">
    <path d="M0 464 Q285.5 600 571 464 L571 976 L0 976 Z" fill="#0d0d0d"/>
  </svg>
  <svg class="back-panel" viewBox="0 0 571 976" width="571" height="976" role="img" aria-label="Small skyline silhouette resting on the curve">
    <defs>
      <linearGradient id="skyline-fade" x1="0" y1="0" x2="0" y2="1">
        <stop offset="0" stop-color="#5a5a5a"/>
        <stop offset="1" stop-color="#0d0d0d"/>
      </linearGradient>
    </defs>
    <path d="M80 497 L80 440 Q284 506 488 441 L488 498 Q284 567 80 497 Z" fill="url(#skyline-fade)"/>
  </svg>
  <div class="brand-mark"></div>
  <h2 class="brand-name"><span class="line-main">HARBOR LANE</span><span class="line-sub">REALTY INC</span></h2>
  <div class="contact">
    <p class="person">Your Name Here</p>
    <p class="title">Title Here</p>
    <p class="address">PO Box 718269 Cedar Marsh<br>FL 32987 Dale Morrick</p>
    <p class="reach"><span class="email">Email : harborlanerealtyinc@mailbox.test</span><br>Phone : 555-271-6094</p>
  </div>
</section>

</body>
</html>
```